Innovative healthcare collaborative needs new look for business cards

CareLoomQ is a new kind of healthcare relationship company focused on aligning partners, innovation and solutions to provide needed health services to healthcare systems, hospitals or private business. Not mired in the old merger and acquisition fee-for-service framework, we focus on primary, secondary and tertiary service area partnership collaboratives. These networks are constructed by aligning healthcare services along a network of care, not just an individual patient care plan. This involves partnership arrangements with large or small medical centers, physician groups, allied health services, public health agencies, health insurers, et al as well as civic agencies, schools, farmers, supply chains to bring about needed healthcare solutions for patients. Think Green Havens. GH does for communities what we do for hospitals and health systems. We educate and instruct on strategic, operational, and innovative solutions for a healthcare provider, practice, business, or system resulting in successful construction of care networks (legal entity). We provide the blueprint of how to do this type of partnership, focused on what’s best for the sustainability of the business and the people (patients or potential patients) living there. Rural hospitals in particular are at risk.
We also provide seminars to academic, medical academic, and private industry to instruct on how to construct these care networks and educate on the essential criteria to be successful in the new healthcare era. We have been doing this work for the past 8 years, and since COVID-19, the recognition of fractured processes has boosted the demand. We need a business card that sets the tone that the traditional healthcare delivery system in the US has transformed (overnight). Our company is educating on how to transition current business models to the new world order in this space.
Brainstormed some business card tag lines for consideration:
CareLoomQ
• a healthcaring company
• allbettertogether
• connecting for the greater good

Target Market(s)

Health systems, hospitals, physician practices, academic medical schools, residency programs

Industry/Entity Type

Healthcare

Contact Information for Business Card

Doreen Vashtoll, Chief Relationship Officer
doreenvashtoll@mailpost-example.net
mobile: 415-286-9043

Font styles to use
Serif
Sans Serif

Requirements
Should not have
• Do not use word Consultant

```html
<!DOCTYPE html>
<html lang="en">
<head>
<meta charset="utf-8">
<title>CareLoomQ Business Card</title>
<link rel="stylesheet" href="https://fonts.googleapis.com/css2?family=Open+Sans:wght@400;600&display=swap">
<style>
  :root {
    --backdrop: #e9eaec;
    --card: #f7f7f5;
    --brand-blue: #4aaee0;
    --text-gray: #7c7f83;
    --logo-gray: #808285;
  }
  html, body {
    margin: 0;
    padding: 0;
    width: 1200px;
    height: 936px;
    overflow: hidden;
    background: var(--backdrop);
  }
  .business-card {
    position: absolute;
    left: 100px;
    top: 163px;
    width: 1000px;
    height: 610px;
    background: var(--card);
    box-shadow: 0 6px 24px rgba(0,0,0,0.12);
    font-family: "Open Sans", sans-serif;
  }
  .brand-name {
    position: absolute;
    right: 40px;
    top: 58px;
    margin: 0;
    font-size: 64px;
    font-weight: 600;
    color: var(--logo-gray);
    letter-spacing: 0.5px;
    line-height: 1;
  }
  .holder {
    position: absolute;
    left: 42px;
    top: 500px;
  }
  .holder-name {
    margin: 0;
    font-size: 38px;
    font-weight: 400;
    color: var(--brand-blue);
    text-transform: uppercase;
    line-height: 1.1;
  }
  .holder-title {
    margin: 4px 0 0;
    font-size: 28px;
    color: var(--text-gray);
    letter-spacing: 0.5px;
  }
  .divider {
    position: absolute;
    left: 455px;
    top: 498px;
    width: 2px;
    height: 66px;
    background: var(--brand-blue);
  }
  .contact-list {
    position: absolute;
    left: 520px;
    top: 494px;
    margin: 0;
    padding: 0;
    list-style: none;
  }
  .contact-item {
    display: flex;
    align-items: center;
    gap: 12px;
    height: 38px;
    color: var(--text-gray);
    font-size: 21px;
  }
  .contact-item.phone { font-size: 26px; }
  .contact-icon { width: 24px; height: 24px; flex: none; }
</style>
</head>
<body>
  <main class="business-card">
    <h1 class="brand-name">CareLoomQ</h1>

    <section class="holder">
      <h2 class="holder-name">Doreen Vashtoll</h2>
      <p class="holder-title">Chief Relationship Officer</p>
    </section>

    <div class="divider"></div>

    <ul class="contact-list">
      <li class="contact-item phone">
        <svg class="contact-icon" viewBox="0 0 24 24" fill="none" stroke="var(--brand-blue)" stroke-width="1.6" stroke-linejoin="round">
          <circle cx="12" cy="12" r="10.5"/>
          <path d="M8.5 7 L10.3 7 L11 9.4 L9.9 10.4 C10.6 12 11.9 13.3 13.5 14 L14.5 12.9 L16.9 13.6 L16.9 15.4 C16.9 16.1 16.3 16.7 15.6 16.6 C11.2 16.2 7.7 12.7 7.3 8.3 C7.2 7.6 7.8 7 8.5 7 Z"/>
        </svg>
        <span>415-286-9043</span>
      </li>
      <li class="contact-item email">
        <svg class="contact-icon" viewBox="0 0 24 24" fill="none" stroke="var(--brand-blue)" stroke-width="1.6" stroke-linejoin="round">
          <rect x="2" y="5" width="20" height="14"/>
          <path d="M2 5 L12 13 L22 5 M2 19 L9.5 11 M22 19 L14.5 11"/>
        </svg>
        <span>doreenvashtoll@mailpost-example.net</span>
      </li>
    </ul>
  </main>
</body>
</html>
```